Web site design for Brivolt Software (www.brivoltsoftware-example.com)

Need the design as well as the html for the website. The brief is given in the attached file.
If possible, would like to use pencil sketches instead of images to give a unique look to the site.
Target Market(s)
small Software product companies
Industry/Entity Type
Software
Coding
Coded - Design and coding required
Number of Pages Required
5+ page

```html
<!DOCTYPE html>
<html lang="en">
<head>
<meta charset="utf-8">
<title>Brivolt Software</title>
<link rel="stylesheet" href="https://fonts.googleapis.com/css2?family=Open+Sans:wght@400;600;700;800&display=swap">
<style>
:root{
  --ink:#2b2b2b;
  --dark:#3a3a3a;
  --footer:#2e2e2e;
  --nav:#3c3c3c;
  --beige:#f2e7da;
  --grey-bg:#efefef;
  --line:#dcdcdc;
  --muted:#555;
  --white:#fff;
  --btn:#3d3d3d;
}
*{box-sizing:border-box;margin:0;padding:0}
html,body{width:1200px;height:4000px;overflow:hidden}
body{position:relative;background:var(--white);font-family:"Open Sans",Arial,sans-serif;color:var(--ink)}
/* header */
.site-header{position:absolute;left:0;top:0;width:1200px;height:93px;background:var(--white)}
.brand{position:absolute;left:99px;top:28px;font-weight:800;font-size:30px;letter-spacing:3px;color:#1d1d1d;text-transform:uppercase}
.top-links{position:absolute;right:99px;top:36px;display:flex;gap:34px;font-size:16px;font-weight:600;color:#222}
.main-nav{position:absolute;left:0;top:93px;width:1200px;height:62px;background:var(--nav);display:flex;align-items:center;padding-left:99px;gap:30px;color:var(--white);font-size:15px;font-weight:700}
.main-nav .caret::after{content:"";display:inline-block;margin-left:7px;border:5px solid transparent;border-top-color:#fff;border-bottom:0;vertical-align:middle}
/* hero */
.hero{position:absolute;left:0;top:155px;width:1200px;height:512px;background:var(--beige);clip-path:polygon(0 0,100% 0,100% 445px,50% 512px,0 445px)}
.hero-title{position:absolute;left:99px;top:105px;font-size:36px;font-weight:800;letter-spacing:3px;color:#222;white-space:nowrap;z-index:2}
.hero-quote{position:absolute;left:99px;top:185px;width:420px;font-size:15px;line-height:24px;color:#333}
.hero-cite{position:absolute;left:99px;top:243px;font-size:15px;font-weight:700;color:#333}
.btn-outline{position:absolute;left:99px;top:324px;width:115px;height:48px;border:2px solid #333;font-size:15px;font-weight:600;display:flex;align-items:center;justify-content:center;color:#222}
.hero-art{position:absolute;left:570px;top:20px;width:600px;height:440px;border-radius:12px;background:radial-gradient(ellipse at center,#ece0d1 0%,var(--beige) 75%)}
/* section heads */
.sec-title{position:absolute;left:0;width:1200px;text-align:center;font-size:25px;font-weight:700;color:#222}
.sec-title::after{content:"";display:block;width:50px;height:2px;background:#333;margin:14px auto 0}
.sec-title.light{color:var(--white)}
.sec-title.light::after{background:var(--white)}
.sec-sub{position:absolute;left:0;width:1200px;text-align:center;font-size:15px;color:#444}
/* services */
.service{position:absolute;top:840px;width:300px;text-align:center}
.service-ring{width:227px;height:227px;margin:0 auto;border-radius:50%;border:3px solid #bdbdbd;padding:14px}
.service-art{width:100%;height:100%;border-radius:50%;background:radial-gradient(circle,#f3f3f3 0%,#e4e4e4 100%)}
.service h3{margin-top:24px;font-size:18px;font-weight:700;color:#222}
.service p{margin:12px auto 0;width:295px;font-size:14px;line-height:21px;color:#444}
.btn-dark{display:inline-flex;align-items:center;justify-content:center;width:92px;height:40px;background:var(--btn);color:var(--white);font-size:13px;font-weight:600;margin-top:18px}
.slider-arrow{position:absolute;top:1035px}
/* about */
.about{position:absolute;left:0;top:1307px;width:1200px;height:720px;background:var(--dark);clip-path:polygon(0 0,50% 60px,100% 0,100% 610px,50% 720px,0 610px)}
.about-copy{position:absolute;left:130px;top:210px;width:940px;text-align:center;color:var(--white);font-size:14px;line-height:30px}
.about-copy p+p{margin-top:12px}
.flow{position:absolute;left:339px;top:380px;width:598px;height:128px;background:linear-gradient(180deg,#ffffff,#f1f6ee)}
/* expertise */
.exp-panels{position:absolute;left:99px;top:2240px;width:1000px;height:227px;display:flex}
.exp-panel{position:relative;flex:1;text-align:center;color:var(--white)}
.exp-panel.left{background:linear-gradient(90deg,#777,#5b5b5b)}
.exp-panel.mid{background:#1f1f1f}
.exp-panel.right{background:linear-gradient(90deg,#4a4a4a,#6e6e6e)}
.exp-badge{position:absolute;left:50%;top:-58px;width:116px;height:116px;margin-left:-58px;border-radius:50%;background:var(--white);display:flex;align-items:center;justify-content:center}
.exp-panel h3{position:absolute;top:98px;width:100%;font-size:20px;font-weight:700}
.exp-panel p{position:absolute;top:140px;left:28px;right:28px;font-size:14px;line-height:22px}
.divider{position:absolute;left:99px;top:2547px;width:1000px;height:2px;background:var(--line)}
/* case studies */
.case-art{position:absolute;left:112px;top:2712px;width:360px;height:250px;border-radius:8px;background:linear-gradient(180deg,#fafafa,#ececec)}
.cases{position:absolute;left:491px;top:2740px;width:620px}
.case h4{font-size:16px;font-weight:600;color:#222;white-space:nowrap}
.case p{margin-top:8px;font-size:13.5px;line-height:20px;color:#555}
.case+.case{margin-top:16px}
/* partners */
.partners{position:absolute;left:0;top:3067px;width:1200px;height:373px;background:var(--grey-bg)}
.partner-row{position:absolute;left:99px;top:226px;width:1002px;display:flex;justify-content:space-between}
.partner{width:160px;height:80px;background:var(--white);border:1px solid #ddd;display:flex;align-items:center;justify-content:center}
.partner span{display:block;width:96px;height:26px;border-radius:4px;background:#d4d4d4}
.partner span.round{width:40px;height:40px;border-radius:50%}
/* footer */
.footer{position:absolute;left:0;top:3387px;width:1200px;height:613px;background:var(--footer);clip-path:polygon(0 0,50% 53px,100% 0,100% 100%,0 100%);color:var(--white)}
.footer h2{position:absolute;left:99px;top:108px;font-size:23px;font-weight:700}
.contact-row{position:absolute;left:99px;display:flex;align-items:center;gap:22px;font-size:15px;line-height:24px}
.contact-icon{width:46px;height:46px;border-radius:50%;border:2px solid #8a8a8a;display:flex;align-items:center;justify-content:center;flex:none}
.form-lead{position:absolute;left:483px;top:112px;font-size:16px}
.field{position:absolute;height:41px;border:2px solid #cfcfcf;background:var(--footer);font-size:13px;padding:11px 10px;color:#eee}
.send{position:absolute;left:483px;top:448px;width:118px;height:36px;background:#8d8d8d;font-size:14px;font-weight:600;display:flex;align-items:center;justify-content:center}
.copyright{position:absolute;left:99px;top:562px;font-size:13px}
.social{position:absolute;left:975px;top:545px;display:flex;gap:8px}
.social span{width:38px;height:38px;border-radius:50%;border:2px solid #bbb}
</style>
</head>
<body>

<header class="site-header">
  <div class="brand">Brivolt Software</div>
  <nav class="top-links"><span>Stories</span><span>Partners</span><span>Giving Back</span><span>Blog</span><span>Contact Us</span></nav>
</header>
<nav class="main-nav">
  <span>Home</span><span class="caret">Services</span><span class="caret">About Us</span><span>Expertise</span><span>Engagement Models</span><span class="caret">Agile</span><span>Our Work</span><span>Work With Us</span><span>Accolades</span>
</nav>

<section class="hero">
  <div class="hero-art" role="img" aria-label="Pencil sketch of the company name surrounded by hand-drawn web, analysis, content, traffic and ranking doodles joined by arrows"></div>
  <h1 class="hero-title">BRIVOLT SOFTWARE</h1>
  <p class="hero-quote">"Perfection is achieved not when there is nothing more to add, but when there is nothing left to take away."</p>
  <p class="hero-cite">–Etienne Marloux</p>
  <div class="btn-outline">Read More</div>
</section>

<h2 class="sec-title" style="top:733px">Our Services</h2>
<svg class="slider-arrow" style="left:26px" width="30" height="66" viewBox="0 0 30 66"><path d="M28 2 L3 33 L28 64" fill="none" stroke="#333" stroke-width="2"/></svg>
<svg class="slider-arrow" style="left:1144px" width="30" height="66" viewBox="0 0 30 66"><path d="M2 2 L27 33 L2 64" fill="none" stroke="#333" stroke-width="2"/></svg>

<div class="service" style="left:125px">
  <div class="service-ring"><div class="service-art" role="img" aria-label="Pencil sketch of a crowd of product ideas"></div></div>
  <h3>BUILD PRODUCT</h3>
  <p>Our team of analysts, design thinkers and technologists work with client and end users to specify and carve out a product.</p>
  <span class="btn-dark">Read More</span>
</div>
<div class="service" style="left:450px">
  <div class="service-ring"><div class="service-art" role="img" aria-label="Pencil sketch of a light bulb and pen for startup entrepreneurs"></div></div>
  <h3>MAINTAIN PRODUCT</h3>
  <p>We have the ability to quickly understand large, legacy products, write scaffold test cases around them, and then maintain.</p>
  <span class="btn-dark">Read More</span>
</div>
<div class="service" style="left:775px">
  <div class="service-ring"><div class="service-art" role="img" aria-label="Pencil sketch of an offshore team setup"></div></div>
  <h3>ODC SETUP</h3>
  <p>We help in setting up Offshore Development centres for small and medium software development companies.</p>
  <span class="btn-dark">Read More</span>
</div>

<section class="about">
  <h2 class="sec-title light" style="top:112px">About Us</h2>
  <div class="about-copy">
    <p>In our belief that a software product's architecture goes a long way in avoiding costly and complex upgrades. Our architecture driven approach makes sure that product upgrades are possible while maintaining productive and friendly user interfaces.</p>
    <p>Whether you are an established software product development company, a startup company or just a person with an idea, we would love to work with you. We work closely with clients to develop top level requirements, design the right team, and implement the software.</p>
  </div>
  <div class="flow" role="img" aria-label="Process diagram: specify, architect and form team, implement, use, gather feedback"></div>
</section>

<h2 class="sec-title" style="top:2053px">Our Expertise</h2>
<p class="sec-sub" style="top:2114px">You need a software product development partner for whom product development work is not just a project</p>
<div class="exp-panels">
  <div class="exp-panel left">
    <div class="exp-badge"><svg width="60" height="44" viewBox="0 0 60 44" fill="#222"><circle cx="16" cy="12" r="7"/><circle cx="44" cy="12" r="7"/><circle cx="30" cy="16" r="8"/><path d="M4 38 C4 26 28 26 28 38 Z"/><path d="M32 38 C32 26 56 26 56 38 Z"/><path d="M16 42 C16 28 44 28 44 42 Z"/></svg></div>
    <h3>Conceptualization</h3>
    <p>Brivolt specializes in taking an idea or a technology and building a product.</p>
  </div>
  <div class="exp-panel mid">
    <div class="exp-badge"><svg width="50" height="54" viewBox="0 0 50 54" fill="none" stroke="#222" stroke-width="4"><circle cx="26" cy="20" r="14"/><path d="M16 31 L5 48"/><circle cx="26" cy="18" r="5" fill="#222" stroke="none"/></svg></div>
    <h3>Product Realization</h3>
    <p>Brivolt specializes in taking an idea or a technology and building a product.</p>
  </div>
  <div class="exp-panel right">
    <div class="exp-badge"><svg width="54" height="54" viewBox="0 0 54 54" fill="none" stroke="#222" stroke-width="3"><path d="M27 14 C18 14 15 22 18 28 C20 32 22 33 22 38 H32 C32 33 34 32 36 28 C39 22 36 14 27 14 Z"/><path d="M23 43 H31 M24 48 H30"/><path d="M27 2 V8 M10 9 L14 13 M44 9 L40 13 M3 25 H9 M45 25 H51"/></svg></div>
    <h3>Technologies</h3>
    <p>Brivolt specializes in taking an idea or a technology and building a product.</p>
  </div>
</div>

<div class="divider"></div>

<h2 class="sec-title" style="top:2604px">Case Studies</h2>
<p class="sec-sub" style="top:2662px">You need a software product development partner for whom product development work is not just a project</p>
<div class="case-art" role="img" aria-label="Line sketch of a team meeting around a table"></div>
<div class="cases">
  <div class="case"><h4>AUTOMATION FOR VARS – NEW PRODUCT DEVELOPMENT</h4><p>VendaFlow is a complete automation system for VARS – it has an ecommerce storefront, customizable catalog, Rich content crawler, Sales Quoting, Integration with Distributor systems, Asset Tracking etc.</p></div>
  <div class="case"><h4>DATA CENTER ASSET TRACKING PRODUCT– NEW PRODUCT DEVELOPMENT</h4><p>RackTrace is an asset tracking and spares system built completely from the ground up to track servers and spares of a Data center, manage warranties, and also integrate with manufacturer websites to seamlessly integrate returns.</p></div>
  <div class="case"><h4>HEALTH CARE PRODUCT – NEW PRODUCT DEVELOPMENT</h4><p>CareLinkOnline is a cloud based Platform for Consumers, Doctors and other healthcare Service Providers, to come together and bring healthcare to consumer's doorstep. Doctors, Consumers, Diagnostic Labs, and Chemists can register.</p></div>
</div>

<section class="partners">
  <h2 class="sec-title" style="top:137px">Our Patrners</h2>
  <div class="partner-row">
    <div class="partner"><span class="round"></span></div>
    <div class="partner"><span></span></div>
    <div class="partner"><span class="round"></span></div>
    <div class="partner"><span class="round"></span></div>
    <div class="partner"><span></span></div>
    <div class="partner"><span class="round"></span></div>
  </div>
</section>

<footer class="footer">
  <h2>CONTACT US</h2>
  <div class="contact-row" style="top:182px">
    <span class="contact-icon"><svg width="22" height="16" viewBox="0 0 22 16" fill="none" stroke="#fff" stroke-width="2"><rect x="1" y="1" width="20" height="14"/><path d="M1 1 L11 9 L21 1"/></svg></span>
    <span>info@brivoltsoftware-example.com</span>
  </div>
  <div class="contact-row" style="top:254px">
    <span class="contact-icon" style="background:#8a8a8a"><svg width="18" height="24" viewBox="0 0 18 24" fill="#fff"><path d="M9 0 C4 0 0 4 0 9 C0 15 9 24 9 24 C9 24 18 15 18 9 C18 4 14 0 9 0 Z M9 13 A4 4 0 1 1 9 5 A4 4 0 1 1 9 13 Z"/></svg></span>
    <span>Office 204, 42 Lakeview Street, Riverside<br>Link Road, &nbsp;Pune India - 411099</span>
  </div>
  <div class="contact-row" style="top:343px">
    <span class="contact-icon"><svg width="22" height="22" viewBox="0 0 24 24" fill="#fff"><path d="M6.6 10.8 C8 13.6 10.4 16 13.2 17.4 L15.4 15.2 C15.7 14.9 16.1 14.8 16.4 15 C17.5 15.4 18.7 15.6 20 15.6 C20.6 15.6 21 16 21 16.6 V20 C21 20.6 20.6 21 20 21 C10.6 21 3 13.4 3 4 C3 3.4 3.4 3 4 3 H7.5 C8.1 3 8.5 3.4 8.5 4 C8.5 5.3 8.7 6.5 9.1 7.6 C9.2 7.9 9.1 8.3 8.9 8.6 Z"/></svg></span>
    <span>+353 (0)86 5550147</span>
  </div>
  <p class="form-lead">Fill out the form below, and we'll contact you shortly.</p>
  <div class="field" style="left:483px;top:234px;width:304px">Your Name</div>
  <div class="field" style="left:803px;top:234px;width:296px">Company</div>
  <div class="field" style="left:483px;top:290px;width:304px">Your Email</div>
  <div class="field" style="left:803px;top:290px;width:296px">Phone</div>
  <div class="field" style="left:483px;top:341px;width:616px;height:89px">How can we help you?</div>
  <div class="send">Send Now</div>
  <p class="copyright">Copyright © 2017 Brivolt Software. All rights reserved</p>
  <div class="social"><span></span><span></span><span></span></div>
</footer>

</body>
</html>
```